Business Card Design Project

I have established a company called "Morrowvale" which is a business specialising in psychotherapy/counselling , predominantly for anxiety & depression.

My name is Tev....hence, the Morrowvale link. However, Morrowvale was also chosen for its reference to green shoots of growth/recovery.

Morrowvale is to be "upmarket" and highly professional. I'm keen for the style and colours to reflect this.....taupe/grey with navy/black script, for example.....NO primary colours.

My name needs to be on the card and my mobile number. Not sure, but suspect it should also have my qualifications ( BA (Psych) & BSc (Hons) Psychology). Mobile number 0491 627 850.

```html
<!DOCTYPE html>
<html lang="en">
<head>
<meta charset="utf-8">
<title>Morrowvale – Business Card</title>
<link rel="stylesheet" href="https://fonts.googleapis.com/css2?family=Didact+Gothic&display=swap">
<style>
  :root {
    --backdrop: #e9e9ec;
    --card-white: #f6f7f6;
    --slate: #5d5e60;
    --slate-text: #626365;
    --leaf: #8aab1c;
    --pale: #e4e5e4;
  }
  * { box-sizing: border-box; margin: 0; padding: 0; }
  html, body {
    width: 1200px;
    height: 934px;
    overflow: hidden;
    background: var(--backdrop);
    font-family: "Didact Gothic", "Century Gothic", sans-serif;
  }
  .sheet {
    position: relative;
    width: 1200px;
    height: 934px;
  }
  .card {
    position: absolute;
    left: 290px;
    width: 620px;
    height: 379px;
    overflow: hidden;
    box-shadow: 0 6px 18px rgba(0,0,0,0.12);
  }
  .card--back {
    top: 60px;
    background: var(--slate);
  }
  .card--front {
    top: 495px;
    background: var(--card-white);
  }
  .wordmark {
    position: absolute;
    font-size: 44px;
    letter-spacing: 3px;
    line-height: 1;
    white-space: nowrap;
  }
  .card--back .wordmark {
    left: 0;
    right: 0;
    top: 168px;
    text-align: center;
    color: var(--pale);
  }
  .card--front .wordmark {
    left: 40px;
    top: 200px;
    font-size: 38px;
    color: var(--slate-text);
  }
  .band {
    position: absolute;
    left: 0;
    top: 0;
    width: 620px;
    height: 379px;
  }
  .holder {
    position: absolute;
    left: 340px;
    top: 70px;
    color: var(--slate-text);
  }
  .holder__name {
    font-size: 23px;
    letter-spacing: 1px;
    font-weight: 400;
  }
  .holder__quals {
    font-size: 10.5px;
    margin-top: 2px;
  }
  .contact {
    position: absolute;
    left: 340px;
    top: 130px;
    font-size: 12.5px;
    line-height: 17px;
    color: var(--slate-text);
  }
  .contact__label {
    color: var(--leaf);
    display: inline-block;
    width: 52px;
  }
  .website {
    position: absolute;
    right: 52px;
    top: 194px;
    font-size: 14px;
    line-height: 18px;
    white-space: nowrap;
    color: var(--slate-text);
  }
  .website__accent { color: var(--leaf); }
</style>
</head>
<body>
<main class="sheet">
  <section class="card card--back" aria-label="Card back">
    <p class="wordmark">MORROWVALE</p>
  </section>

  <section class="card card--front" aria-label="Card front">
    <svg class="band" viewBox="0 0 620 379" aria-hidden="true">
      <path d="M0 352 C210 338 430 306 620 254 L620 379 L0 379 Z" fill="var(--slate)"/>
      <path d="M0 340 C200 326 430 294 614 250" fill="none" stroke="var(--leaf)" stroke-width="6" stroke-linecap="round"/>
    </svg>

    <p class="wordmark">MORROWVALE</p>

    <div class="holder">
      <h1 class="holder__name">TEV HARLOW</h1>
      <p class="holder__quals">BA (Psych) BSc (Hons) Psych MBPS</p>
    </div>

    <p class="contact">
      <span class="contact__label">Mobile:</span>0491 627 850<br>
      <span class="contact__label">E-mail:</span>tev.harlow@mailbridge.com
    </p>

    <p class="website">www.<span class="website__accent">morrowvaleconsulting</span>.com.au</p>
  </section>
</main>
</body>
</html>
```